" A maioria das empresas tem dificuldades em lidar com o quadro de funcionários. A consultoria entra fornecendo todo o suporte com treinamentos para melhoria do clima e das relações interpessoais, melhoria do atendimento ao cliente, desenvolve líderes e os capacita para lidar de maneira mais adequada com os conflitos da equipe. Além disso, também realizamos todo o processo de recrutamento e seleção. Entre outros serviços. "

```html
<!DOCTYPE html>
<html lang="pt-BR">
<head>
<meta charset="UTF-8">
<title>Vertice – Assinatura de e-mail</title>
<link href="https://fonts.googleapis.com/css2?family=Open+Sans:wght@400;600;700&display=swap" rel="stylesheet">
<style>
  :root{
    --navy:#101b3f;
    --gold:#f2b22a;
    --white:#ffffff;
    --ink:#1d1d26;
    --muted:#555a66;
    --page:#ececec;
  }
  *{margin:0;padding:0;box-sizing:border-box}
  html,body{width:1200px;height:1200px;overflow:hidden;background:var(--page);font-family:"Open Sans",Arial,sans-serif}
  .signature{position:absolute;left:24px;top:468px;width:1156px;height:252px;background:var(--white);border-radius:48px 0 0 0;overflow:hidden}
  .brand-panel{position:absolute;left:0;top:0;width:408px;height:100%;background:var(--navy)}
  .brand{position:absolute;left:48px;top:98px;display:flex;align-items:center;gap:14px}
  .brand-dot{width:30px;height:30px;background:var(--gold);border-radius:50%}
  .brand-name{color:var(--white);font-weight:600;font-size:50px;letter-spacing:1px;line-height:1}
  .brand-tagline{position:absolute;left:92px;top:160px;color:var(--gold);font-size:18px;letter-spacing:1px;white-space:nowrap}
  .accent-bar{position:absolute;left:420px;top:14px;width:8px;height:224px;background:var(--gold)}
  .person{position:absolute;left:461px;top:34px}
  .person-name{font-weight:700;font-size:19px;letter-spacing:2px;color:var(--ink);white-space:nowrap}
  .person-role{font-size:13px;color:var(--gold);margin-top:1px}
  .office-phone{position:absolute;left:461px;top:94px;display:flex;align-items:center;gap:12px;font-size:19px;color:var(--ink)}
  .social{position:absolute;left:461px;top:184px;display:flex;flex-direction:column;gap:12px}
  .social-item{display:flex;align-items:center;gap:10px;font-size:15px;color:var(--muted)}
  .social-mark{width:16px;height:16px;background:var(--gold);border-radius:3px}
  .contacts{position:absolute;right:72px;top:36px;text-align:right;font-size:19px;color:var(--ink);line-height:33px;white-space:nowrap}
  .address{position:absolute;right:72px;top:196px;text-align:right;font-size:14px;color:var(--ink);line-height:22px;white-space:nowrap}
  .icon-strip{position:absolute;right:0;top:0;width:58px;height:100%;background:var(--navy)}
  .icon-strip svg{position:absolute;left:19px}
</style>
</head>
<body>
  <section class="signature">
    <div class="brand-panel">
      <div class="brand">
        <span class="brand-dot"></span>
        <span class="brand-name">VERTICE</span>
      </div>
      <div class="brand-tagline">Gestão com Propósito</div>
    </div>
    <div class="accent-bar"></div>

    <div class="person">
      <div class="person-name">RAFAEL MOURA DUARTE</div>
      <div class="person-role">Cargo/Função</div>
    </div>

    <div class="office-phone">
      <svg width="16" height="16" viewBox="0 0 24 24"><path fill="#1d1d26" d="M6.6 10.8a15 15 0 0 0 6.6 6.6l2.2-2.2a1 1 0 0 1 1-.25 11.4 11.4 0 0 0 3.6.57 1 1 0 0 1 1 1V20a1 1 0 0 1-1 1A17 17 0 0 1 3 4a1 1 0 0 1 1-1h3.5a1 1 0 0 1 1 1c0 1.25.2 2.45.57 3.57a1 1 0 0 1-.25 1z"/></svg>
      <span>(31) 3000-5678</span>
    </div>

    <div class="social">
      <div class="social-item"><span class="social-mark"></span><span>/verticeconsult</span></div>
      <div class="social-item"><span class="social-mark"></span><span>@verticeconsult</span></div>
    </div>

    <div class="contacts">
      <div>(31) 90000-1234</div>
      <div>(31) 90000-1234</div>
      <div>contato@verticeconsult.com.br</div>
      <div>www.verticeconsult.com.br</div>
    </div>
    <div class="address">
      <div>Av. das Acácias, N° 512 - Bairro</div>
      <div>Cidade/UF CEP: 30100-200</div>
    </div>

    <div class="icon-strip">
      <svg style="top:44px" width="20" height="20" viewBox="0 0 24 24"><path fill="#fff" d="M6.6 10.8a15 15 0 0 0 6.6 6.6l2.2-2.2a1 1 0 0 1 1-.25 11.4 11.4 0 0 0 3.6.57 1 1 0 0 1 1 1V20a1 1 0 0 1-1 1A17 17 0 0 1 3 4a1 1 0 0 1 1-1h3.5a1 1 0 0 1 1 1c0 1.25.2 2.45.57 3.57a1 1 0 0 1-.25 1z"/></svg>
      <svg style="top:76px" width="20" height="20" viewBox="0 0 24 24"><circle cx="12" cy="12" r="8" fill="#fff"/></svg>
      <svg style="top:109px" width="20" height="20" viewBox="0 0 24 24"><rect x="2" y="5" width="20" height="14" rx="1.5" fill="#fff"/><path d="M3 6l9 7 9-7" fill="none" stroke="#101b3f" stroke-width="1.8"/></svg>
      <svg style="top:142px" width="20" height="20" viewBox="0 0 24 24"><rect x="6" y="6" width="12" height="12" rx="2" fill="#fff"/></svg>
      <svg style="top:200px" width="20" height="20" viewBox="0 0 24 24"><path fill="#fff" d="M12 2a7 7 0 0 0-7 7c0 5.2 7 13 7 13s7-7.8 7-13a7 7 0 0 0-7-7zm0 9.5A2.5 2.5 0 1 1 12 6.5a2.5 2.5 0 0 1 0 5z"/></svg>
    </div>
  </section>
</body>
</html>
```